Letterhead Design Project

Attached is our new Logo and a copy of our old letter head
Looking to rebrand with our new logo

Reason: I want to show a business card design

Industry/Entity Type

Film Production

Colors

Designer to choose colors to be used in the design.

Requirements
Must have
• The information on the old letterhead

```html
<!DOCTYPE html>
<html lang="en">
<head>
<meta charset="utf-8">
<title>Kestrel International Letterhead</title>
<link rel="stylesheet" href="https://fonts.googleapis.com/css2?family=Libre+Franklin:ital,wght@0,400;0,600;1,400&display=swap">
<style>
  :root {
    --ink: #0f5a78;
    --brand: #1a8fc4;
    --accent: #ef6a2e;
    --paper: #ffffff;
  }
  html, body {
    margin: 0;
    padding: 0;
    overflow: hidden;
    background: var(--paper);
  }
  .letterhead {
    position: relative;
    width: 927px;
    height: 1200px;
    background: var(--paper);
    font-family: "Libre Franklin", Arial, sans-serif;
    color: var(--ink);
    overflow: hidden;
  }
  .masthead {
    position: absolute;
    top: 58px;
    left: 0;
    right: 0;
    text-align: center;
  }
  .brand-name {
    display: inline-flex;
    align-items: center;
    gap: 12px;
    font-size: 44px;
    font-weight: 600;
    color: var(--brand);
    letter-spacing: 0.5px;
    margin: 0 0 36px;
    line-height: 1;
  }
  .brand-dot {
    width: 16px;
    height: 16px;
    border-radius: 50%;
    background: var(--accent);
  }
  .services {
    font-weight: 600;
    font-size: 16px;
    margin: 0 0 6px;
  }
  .contact-line {
    font-size: 16px;
    margin: 0 0 6px;
  }
  .sep {
    display: inline-block;
    width: 7px;
    height: 7px;
    border-radius: 50%;
    background: var(--accent);
    vertical-align: middle;
    margin: 0 6px 2px;
  }
  .divisions {
    position: absolute;
    top: 1091px;
    left: 0;
    right: 0;
    text-align: center;
    font-size: 16px;
    font-weight: 600;
  }
  .division-mark {
    color: var(--brand);
    margin-right: 4px;
  }
  .legal {
    position: absolute;
    top: 1135px;
    left: 0;
    right: 0;
    text-align: center;
    font-style: italic;
    font-size: 16px;
    line-height: 22px;
  }
  .legal p { margin: 0; }
</style>
</head>
<body>
<div class="letterhead">
  <header class="masthead">
    <h1 class="brand-name"><span class="brand-dot"></span>Kestrel International</h1>
    <p class="services">Supply<span class="sep"></span>Management of Infrastructure<span class="sep"></span>Logistics</p>
    <p class="contact-line">P.O. Box 482 Marlow QLD 4390<span class="sep"></span>P.O. Box 317 Elmvale NSW 2195</p>
    <p class="contact-line">Phone: 0400 123 456<span class="sep"></span>Email: hello@kestrelintl.com.au</p>
  </header>

  <footer>
    <div class="divisions">
      <span class="division-mark">Kestrel</span> Film Services<span class="sep"></span>
      <span class="division-mark">Kestrel</span> Pilot Escorts<span class="sep"></span>
      <span class="division-mark">Kestrel</span> Tour Management<span class="sep"></span>
      <span class="division-mark">Kestrel</span> Driver
    </div>
    <div class="legal">
      <p>are divisions of Kestrel International Pty Ltd</p>
      <p>ACN 987 654 321<span class="sep"></span>ABN 12 987 654 321</p>
    </div>
  </footer>
</div>
</body>
</html>
```